Sunny Paths and joy Business card

I have a logo, but will like a business card design. Is for a travel agency in Mexico. We focus in family experiences.

I will liek some thing different and unique, from the traditional business card, something to get remmeber for.

Business card information:

Leandro T. Ocampo
leandro@sunnypathsjoy.example

Alameda 482, 3 piso
Col. Tlalpizco
Mexico, D.F. 07320

office: (55) 5000-0142
mobile: (55) 9000-0187

www.sunnypathsjoy.example
@sunnypjoy
blog: sunnypathsandjoy.blogsite.example
facebook: SunnyPathsAndJoy

```html
<!DOCTYPE html>
<html lang="en">
<head>
<meta charset="utf-8">
<title>Sunny Paths and joy – Business card</title>
<link rel="stylesheet" href="https://fonts.googleapis.com/css2?family=Ubuntu:wght@400;500;700&display=swap">
<style>
  :root {
    --navy: #145482;
    --navy-deep: #0f4a7a;
    --sky-pale: #b7daf2;
    --sky-mid: #6fa5d8;
    --ink: #3d3d3d;
    --name-blue: #1d5a8a;
    --ghost: #2a6596;
    --paper: #ffffff;
  }
  * { box-sizing: border-box; margin: 0; padding: 0; }
  html, body { width: 1200px; height: 900px; overflow: hidden; background: var(--paper); }
  body { position: relative; font-family: "Ubuntu", sans-serif; }

  .card {
    position: absolute;
    left: 273px;
    width: 644px;
    height: 367px;
    border-radius: 22px;
    overflow: hidden;
    box-shadow: 4px 6px 8px rgba(0,0,0,0.45);
  }
  .card-front { top: 48px; background: var(--navy); }
  .card-back { top: 485px; background: var(--paper); }
  .card svg.backdrop { position: absolute; inset: 0; }

  .brand-name {
    position: absolute;
    font-weight: 700;
    color: var(--navy-deep);
    text-align: center;
    line-height: 1;
  }
  .card-front .brand-name { left: 0; width: 644px; top: 236px; font-size: 44px; }
  .front-web {
    position: absolute; left: 0; width: 644px; top: 328px;
    text-align: center; color: var(--paper); font-size: 18px;
  }
  .front-web b { font-weight: 700; }

  .card-back .brand-name { left: 20px; width: 270px; top: 118px; font-size: 34px; line-height: 1.05; }
  .ghost-name {
    position: absolute; left: 330px; top: 60px; width: 400px;
    font-weight: 700; font-size: 66px; line-height: 1; color: var(--ghost);
    white-space: nowrap;
  }

  .holder {
    position: absolute; right: 372px; top: 232px;
    font-size: 20px; font-weight: 700; color: var(--name-blue);
  }
  .contact-list { position: absolute; right: 360px; top: 270px; list-style: none; text-align: right; }
  .contact-list li { font-size: 16px; color: var(--ink); height: 21.5px; display: flex; justify-content: flex-end; align-items: center; gap: 5px; }
  .contact-list svg { width: 12px; height: 12px; fill: var(--name-blue); }

  .address { position: absolute; left: 333px; top: 168px; color: var(--paper); font-size: 16px; line-height: 22px; font-style: normal; }
  .links { position: absolute; left: 338px; top: 249px; list-style: none; color: var(--paper); font-size: 16px; }
  .links li { height: 21.5px; display: flex; align-items: center; gap: 7px; }
  .links .dot { width: 11px; height: 11px; border-radius: 50%; background: var(--sky-pale); flex: none; }
  .links svg { width: 11px; height: 11px; flex: none; }
</style>
</head>
<body>

<section class="card card-front" aria-label="Card front">
  <svg class="backdrop" width="644" height="367" viewBox="0 0 644 367">
    <path d="M0 285 C 200 240, 420 150, 644 145 L 644 367 L 0 367 Z" fill="var(--sky-pale)"/>
    <path d="M0 305 C 200 270, 430 215, 644 219 L 644 367 L 0 367 Z" fill="var(--sky-mid)"/>
    <circle cx="313" cy="152" r="76" fill="var(--sky-pale)"/>
  </svg>
  <div class="brand-name">Sunny Paths and joy</div>
  <p class="front-web">www.<b>sunnypathsjoy</b>.example</p>
</section>

<section class="card card-back" aria-label="Card back">
  <svg class="backdrop" width="644" height="367" viewBox="0 0 644 367">
    <rect x="309" y="0" width="335" height="367" fill="var(--navy)"/>
    <rect x="309" y="0" width="6" height="367" fill="var(--sky-mid)"/>
    <circle cx="140" cy="105" r="50" fill="var(--sky-pale)" opacity="0.6"/>
    <rect x="300" y="236" width="18" height="18" transform="rotate(45 309 245)" fill="var(--sky-mid)"/>
  </svg>
  <div class="ghost-name" aria-hidden="true">Sunny Paths<br>and joy</div>
  <div class="brand-name">Sunny Paths<br>and joy</div>

  <h1 class="holder">Leandro T. Ocampo</h1>
  <ul class="contact-list">
    <li>(55) 5000-0142 <svg viewBox="0 0 12 12"><path d="M2.5 1 L4.5 1 L5.3 3.6 L4 4.6 C4.6 6 5.9 7.3 7.4 8 L8.4 6.7 L11 7.5 L11 9.5 C11 10.4 10.3 11 9.5 11 C5 10.7 1.3 7 1 2.5 C1 1.7 1.6 1 2.5 1 Z"/></svg></li>
    <li>(55) 9000-0187 <svg viewBox="0 0 12 12"><path d="M3.5 0.5 H8.5 A1 1 0 0 1 9.5 1.5 V10.5 A1 1 0 0 1 8.5 11.5 H3.5 A1 1 0 0 1 2.5 10.5 V1.5 A1 1 0 0 1 3.5 0.5 Z M4 2 V9 H8 V2 Z"/></svg></li>
    <li>leandro@sunnypathsjoy.example <svg viewBox="0 0 12 12"><path d="M1 2.5 H11 V3.2 L6 6.5 L1 3.2 Z M1 4.4 L6 7.7 L11 4.4 V9.5 H1 Z"/></svg></li>
  </ul>

  <address class="address">Alameda 482, 3 piso<br>Col. Tlalpizco<br>Mexico, D.F. 07320</address>
  <ul class="links">
    <li><span class="dot"></span>@sunnypjoy</li>
    <li><span class="dot"></span>sunnypathsandjoy.blogsite.example</li>
    <li><span class="dot"></span>SunnyPathsAndJoy</li>
    <li><svg viewBox="0 0 12 12" fill="none" stroke="var(--sky-pale)" stroke-width="1.1"><circle cx="6" cy="6" r="5"/><ellipse cx="6" cy="6" rx="2.2" ry="5"/><path d="M1 6 H11 M2 3.3 H10 M2 8.7 H10"/></svg>www.sunnypathsjoy.example</li>
  </ul>
</section>

</body>
</html>
```